Zentra Logo & Package Design

Hello!

I’m starting a new business. Basically, I’m creating a line of products.

The first product I’m focusing on is Toilet Paper.

The design of this company will be that 75% of our profits will be forwarded to charity (various charities).

I have shortlisted 4 names. Use which one you think is the best.

Please create a clean, minimal and appropriate LOGO for this company.

Here’s a brief breakdown of the names:
----
1. Pinecrestwood --- Simply describes the 75% part of the business. PW is also a good acronym. Maybe the name can be pinecrestwood, and then we can use PW for the packaging.

2. Harbor Lantern --- Simply describes the 75% part of the business.

3. Quiet Amber Fields --- One of my favourite Tomas Vreeland songs, and I thought it would be a good name.

4. Marvelstone or 'marvel stone' (2 words) --- I just like this name/concept.
----

I value the creative process, and feedback from creators. So if you have any thoughts, please feel free to leave a comment in the Public Board, and I will do my best to provide immediate feedback and clarification throughout this process.

I’m very excited to get started on all this.

Thanks!

```html
<!DOCTYPE html>
<html lang="en">
<head>
<meta charset="utf-8">
<title>Pinecrestwood Toilet Paper Wrap</title>
<link rel="stylesheet" href="https://fonts.googleapis.com/css2?family=Sansita:ital,wght@1,800&family=Comfortaa:wght@500;700&display=swap">
<style>
  :root {
    --page-bg: #eef0f3;
    --wrap-bg: #ffffff;
    --petal-pink: #e89aae;
    --petal-soft: #f6d3dc;
    --band-pink: #f1c9d6;
    --band-light: #f9e6ed;
    --title-purple: #8a2c8e;
    --text-dark: #2b2b33;
    --brand-orange: #ea7b1e;
  }
  * { margin: 0; padding: 0; box-sizing: border-box; }
  html, body {
    width: 816px;
    height: 1200px;
    overflow: hidden;
    background: var(--page-bg);
  }
  .wrap-label {
    position: absolute;
    left: 38px;
    top: 342px;
    width: 740px;
    height: 516px;
    background: var(--wrap-bg);
    overflow: hidden;
    box-shadow: 0 6px 18px rgba(40, 40, 60, 0.18);
  }
  .petal-backdrop {
    position: absolute;
    inset: 0;
    background:
      radial-gradient(ellipse 60px 28px at 380px 40px, var(--petal-pink), transparent 75%),
      radial-gradient(ellipse 55px 22px at 300px 190px, var(--petal-soft), transparent 80%),
      radial-gradient(ellipse 70px 40px at 40px 40px, var(--petal-soft), transparent 80%),
      radial-gradient(ellipse 90px 60px at 150px 300px, var(--petal-soft), transparent 80%),
      radial-gradient(ellipse 55px 20px at 290px 445px, var(--petal-pink), transparent 75%),
      radial-gradient(ellipse 60px 80px at 720px 60px, var(--petal-pink), transparent 75%),
      radial-gradient(ellipse 50px 90px at 720px 300px, var(--petal-soft), transparent 80%),
      radial-gradient(ellipse 30px 20px at 470px 220px, var(--petal-soft), transparent 80%),
      var(--wrap-bg);
  }
  .brand-band {
    position: absolute;
    left: 492px;
    top: 0;
    width: 182px;
    height: 100%;
    background: linear-gradient(180deg, var(--band-pink) 0%, var(--band-light) 55%, var(--wrap-bg) 100%);
    border-left: 6px solid var(--wrap-bg);
    border-right: 6px solid var(--wrap-bg);
  }
  .product-title {
    position: absolute;
    left: 66px;
    top: 88px;
    font-family: "Sansita", "Trebuchet MS", sans-serif;
    font-style: italic;
    font-weight: 800;
    font-size: 30px;
    letter-spacing: 1px;
    color: var(--title-purple);
  }
  .title-rule {
    position: absolute;
    left: 68px;
    top: 136px;
    width: 230px;
    height: 2px;
    background: var(--title-purple);
  }
  .product-claim {
    position: absolute;
    left: 68px;
    top: 148px;
    font-family: "Comfortaa", "Helvetica", sans-serif;
    font-weight: 500;
    font-size: 13px;
    color: var(--text-dark);
  }
  .product-feature {
    position: absolute;
    left: 68px;
    top: 170px;
    font-family: "Comfortaa", "Helvetica", sans-serif;
    font-weight: 700;
    font-size: 21px;
    color: var(--text-dark);
  }
  .brand-mark {
    position: absolute;
    left: 498px;
    top: 360px;
    width: 170px;
    text-align: center;
  }
  .brand-dot {
    display: block;
    width: 46px;
    height: 46px;
    margin: 0 auto 12px;
    border-radius: 50%;
    background: var(--brand-orange);
  }
  .brand-name {
    font-family: "Comfortaa", "Helvetica", sans-serif;
    font-weight: 700;
    font-size: 15px;
    letter-spacing: 0.5px;
    color: var(--brand-orange);
  }
  .charity-note {
    position: absolute;
    left: 498px;
    top: 466px;
    width: 170px;
    text-align: right;
    padding-right: 8px;
    font-family: "Comfortaa", "Helvetica", sans-serif;
    font-weight: 700;
    font-size: 8px;
    line-height: 1.5;
    color: var(--text-dark);
  }
</style>
</head>
<body>
  <div class="wrap-label">
    <div class="petal-backdrop" role="img" aria-label="Soft focus photograph of pink rose petals drifting on white"></div>
    <div class="brand-band"></div>
    <h1 class="product-title">TOYLET PEPAR</h1>
    <div class="title-rule"></div>
    <p class="product-claim">Filled with thefragrance of roses</p>
    <p class="product-feature">Super Soft</p>
    <div class="brand-mark">
      <span class="brand-dot"></span>
      <span class="brand-name">PINECRESTWOOD</span>
    </div>
    <p class="charity-note">75% Of Our Profits Will Be Forwarded<br>To Charity (Various Charities)</p>
  </div>
</body>
</html>
```